Roofing Company needs YOU to help put us on top!

Brightpeak Roofing, a fresh new company with quality and Innovation in mind, needs your help to stand out in the competitive Chicago market. With over 30 years of experience, all the right people and tools for the job, the only thing we are missing is your creative ideas in web design to help us grow our online presence.
Our Company offers exceptional quality at reasonable prices, we work for the everyday people both blue collar and white collar.

We have used Craftswarm in the past with multiple successful campaigns, we are excited to see what you can come up with for our website.

www.BrightpeakRoofing.example will be the domain

We will be hiring a photographer for visual content on our pages later. Stock photos are okay to use but should follow theme.

Thank you for taking the time on the submissions, if you have any questions don't hesitate to ask and we will provide whatever is needed to you.

Target Market(s)

Homeowners & Commercial Clients between 21-65

Industry/Entity Type

Roofing

Coding

Coded - Design and coding required

Number of Pages Required

4 page

Font styles to use
Sans Serif

Colors
ffffff
ec1f27
000000
5c5c5c
757575
b2b2b2

Requirements
Must have
• Color Scheme - should follow around our logo
• As for pages we were looking for an About, Services, Projects (gallery page) and Contact.
• Main page please include social media links and a a place so people could use tillbee to make payments
• Website should work on desktop as well as mobile platforms
Nice to have
• A Live chat feature would be nice if possible
Should not have
• Obscure Colors or Common web templates

```html
<!DOCTYPE html>
<html lang="en">
<head>
<meta charset="utf-8">
<title>Brightpeak Roofing — About</title>
<link href="https://fonts.googleapis.com/css2?family=Montserrat:wght@500;600;700;800&family=Open+Sans:wght@400;600;700&display=swap" rel="stylesheet">
<style>
:root{
  --red:#ec1f27;
  --black:#000000;
  --white:#ffffff;
  --grey-dark:#5c5c5c;
  --grey:#757575;
  --grey-light:#b2b2b2;
  --band:#ececec;
  --frame:#e6e6e6;
  --head:"Montserrat",sans-serif;
  --body:"Open Sans",sans-serif;
}
*{box-sizing:border-box;margin:0;padding:0}
html,body{width:1200px;height:2423px;overflow:hidden}
body{background:var(--frame);font-family:var(--body);color:#222}
.page{position:absolute;left:16px;top:12px;width:1168px;height:2394px;background:var(--white);overflow:hidden}

/* header */
.site-header{position:relative;height:149px}
.topbar{position:absolute;right:0;top:0;width:620px;height:40px;background:var(--red);clip-path:polygon(28px 0,100% 0,100% 100%,0 100%);display:flex;align-items:center;padding-left:48px;gap:22px;color:var(--white);font:700 15px var(--head)}
.topbar .phone{display:flex;align-items:center;gap:8px}
.topbar .phone svg{width:18px;height:18px}
.social{display:flex;gap:5px;margin-left:14px}
.social span{width:20px;height:20px;border:2px solid var(--white);border-radius:50%}
.brand{position:absolute;left:28px;top:58px;display:flex;align-items:center;gap:12px}
.brand .mark{width:26px;height:26px;background:var(--red)}
.brand .name{font:800 38px/1 var(--head);color:var(--black);letter-spacing:-.5px}
.main-nav{position:absolute;right:18px;top:100px;display:flex;align-items:center;gap:22px;font:700 14px var(--head);color:var(--black);text-transform:uppercase}
.main-nav .active{color:var(--red);border-bottom:3px solid var(--red);padding-bottom:3px}
.main-nav .cta{background:var(--black);color:var(--white);padding:8px 12px;border-radius:3px}
.service-nav{height:42px;background:var(--black);display:flex;align-items:center;justify-content:space-between;padding:0 42px 0 58px;color:var(--white);font:700 14px var(--head);text-transform:uppercase}

/* hero */
.hero{position:relative;height:512px}
.hero-photo{position:absolute;inset:0;background:linear-gradient(180deg,#6fa9d8 0%,#a8c7de 22%,#8d7465 48%,#6e5648 100%)}
.quote-form{position:absolute;left:779px;top:50px;width:315px;height:377px;background:var(--white);box-shadow:0 2px 8px rgba(0,0,0,.3);padding:82px 16px 0 16px}
.quote-form h2{position:absolute;left:-10px;top:22px;width:325px;height:48px;background:var(--red);color:var(--white);font:700 19px/48px var(--head);text-align:center}
.field{display:flex;gap:8px;margin-bottom:8px}
.field .icon{width:34px;height:34px;border:1px solid #ccc;background:#f3f3f3;border-radius:3px;display:flex;align-items:center;justify-content:center}
.field .icon svg{width:16px;height:16px;fill:var(--grey-dark)}
.field .input{flex:1;height:34px;border:1px solid #ccc;background:#f3f3f3;border-radius:3px;font:700 11px/34px var(--head);color:#444;padding-left:12px;position:relative}
.field .input.select::after{content:"";position:absolute;right:10px;top:13px;border:6px solid transparent;border-top-color:var(--grey-dark)}
.field .input.area{height:66px;line-height:26px}
.field.tall .icon{height:34px}
.quote-form .submit{display:block;width:188px;height:28px;margin:14px auto 0;background:var(--black);color:var(--white);font:700 13px/28px var(--head);text-align:center;border-radius:2px}
.tagline{position:relative;height:105px;background:linear-gradient(180deg,#2a2a2a,#111);color:var(--white);font:700 31px/105px var(--head);text-align:center;box-shadow:0 12px 14px -8px rgba(0,0,0,.45)}
.tagline em{font-style:normal;color:var(--red)}

/* section heading */
.section-title{display:flex;align-items:center;justify-content:center;gap:16px}
.section-title::before,.section-title::after{content:"";height:1px;width:190px;background:#ccc}
.section-title h2{font:700 26px var(--head);color:var(--grey-dark);text-transform:uppercase;white-space:nowrap}
.section-title h2 span{color:var(--black)}

/* about */
.about{height:500px;padding-top:88px;position:relative}
.about-text{position:absolute;left:52px;top:152px;width:525px;font:13.5px/1.55 var(--body);color:#222}
.about-text p{margin-bottom:19px}
.about-text .sign{font:600 17px var(--body);color:var(--black)}
.about-photo{position:absolute;left:650px;top:148px;width:470px;height:288px;border:1px solid #ddd;padding:4px;background:var(--white);box-shadow:0 1px 4px rgba(0,0,0,.12)}
.about-photo div{width:100%;height:100%;background:linear-gradient(180deg,#c9d5dc 0%,#b9c6cd 40%,#c98b5e 70%,#a8603a 100%)}

/* links band */
.links-band{height:185px;background:var(--band);display:flex;justify-content:center;align-items:center;gap:70px}
.link-pill{position:relative;width:320px;height:90px}
.link-pill .pill{position:absolute;left:70px;top:23px;width:250px;height:44px;border:2px solid var(--red);border-radius:0 10px 10px 0;background:var(--white);font:700 16px/40px var(--head);color:#333;text-align:center;padding-left:20px}
.link-pill .disc{position:absolute;left:0;top:0;width:90px;height:90px;border-radius:50%;background:var(--red);border:5px solid var(--white);box-shadow:0 0 0 1px #ddd;display:flex;align-items:center;justify-content:center}
.link-pill .disc svg{width:46px;height:40px;fill:none;stroke:var(--white);stroke-width:3}

/* advantages */
.advantages{position:relative;height:525px;padding-top:84px}
.adv-list{position:absolute;left:40px;top:150px;width:1090px;display:flex;justify-content:space-between}
.adv{width:150px;text-align:center;font:700 11.5px/1.35 var(--body);color:#333}
.adv.up{margin-top:0}.adv.down{margin-top:48px}
.adv .ring{width:122px;height:122px;margin:0 auto 10px;border-radius:50%;border:7px solid var(--black);border-bottom-color:var(--red);border-left-color:var(--red);transform:rotate(-45deg);display:flex;align-items:center;justify-content:center}
.adv .ring .core{width:92px;height:92px;border-radius:50%;background:var(--red);transform:rotate(45deg);display:flex;align-items:center;justify-content:center;box-shadow:0 0 0 5px #f2f2f2}
.adv .ring svg{width:50px;height:50px;fill:none;stroke:var(--white);stroke-width:3;stroke-linejoin:round}
.footer-brand{position:absolute;left:0;right:0;bottom:-18px;text-align:center;font:800 46px/1 var(--head);color:var(--grey-dark);z-index:2}

/* footer */
.site-footer{position:relative;height:344px;background:var(--black);color:var(--white)}
.fcol{position:absolute;top:118px}
.fcol h3{font:700 14px var(--head);color:var(--red);text-transform:uppercase;padding-bottom:10px;border-bottom:1px solid #444;margin-bottom:18px}
.fcol ul{list-style:none;font:600 12px/1.65 var(--body);text-transform:uppercase}
.fcol li::before{content:"· "}
.col-links{left:60px;width:175px}
.col-services{left:292px;width:290px}
.col-services .lists{display:flex;gap:50px}
.col-contact{left:640px;width:170px}
.col-contact .line{display:flex;gap:10px;font:600 12.5px/1.75 var(--body);margin-bottom:14px}
.col-contact svg{width:18px;height:18px;flex:none;margin-top:3px;fill:none;stroke:var(--white);stroke-width:1.6}
.contact-box{position:absolute;left:862px;top:120px;width:274px;height:190px;background:var(--red);border:2px solid var(--white);border-radius:6px;padding:14px 0 0 40px;box-shadow:0 0 0 1px var(--red)}
.contact-box h3{font:700 17px var(--head);color:var(--black);margin-bottom:8px;margin-left:6px}
.cb-phone{display:flex;align-items:center;gap:8px;margin-bottom:8px}
.cb-phone svg{width:26px;height:26px;fill:none;stroke:var(--white);stroke-width:1.8}
.cb-phone small{display:block;font:700 11px/1 var(--head);text-transform:uppercase}
.cb-phone strong{display:block;font:700 22px/1.1 var(--head)}
.contact-box .btn{display:block;width:176px;height:26px;background:var(--black);font:700 12px/26px var(--head);text-align:center;margin:12px 0 0 10px}
.legal{height:32px;background:#d4d4d4;display:flex;align-items:center;justify-content:space-between;padding:0 16px;font:600 10px var(--body);color:#555;text-transform:uppercase}
.legal .social span{border-color:#777;width:18px;height:18px}
</style>
</head>
<body>
<div class="page">

  <header class="site-header">
    <div class="topbar">
      <span class="phone"><svg viewBox="0 0 24 24"><circle cx="12" cy="12" r="11" fill="none" stroke="#fff" stroke-width="2"/><path d="M8 6l2 3-1.5 1.5a8 8 0 0 0 5 5L15 14l3 2-1.5 2.5C11 18 6 13 5.5 7.5z" fill="#fff"/></svg>ILLINOIS 708-555-0142</span>
      <span>INDIANA 219-555-0187</span>
      <span class="social"><span></span><span></span><span></span><span></span><span></span></span>
    </div>
    <a class="brand"><span class="mark"></span><span class="name">BRIGHTPEAK ROOFING</span></a>
    <nav class="main-nav">
      <span>Home</span><span class="active">About</span><span>Projects</span><span>Contact</span><span class="cta">Request a Quote</span>
    </nav>
  </header>

  <nav class="service-nav">
    <span>Shingle Roofs</span><span>Flat Roofs</span><span>Roof Repairs</span><span>Storm Damage</span><span>Insurance Work</span><span>Gutters</span><span>Carpentry</span><span>Windows</span><span>Kitchens and Baths</span>
  </nav>

  <section class="hero">
    <div class="hero-photo" role="img" aria-label="Photo of a roofer in a hard hat and safety harness working on a shingle roof under a blue sky"></div>
    <form class="quote-form">
      <h2>GET INSTANT ONLINE QUOTE</h2>
      <div class="field"><span class="icon"><svg viewBox="0 0 16 16"><circle cx="8" cy="5" r="3.5"/><path d="M1 16c0-4 3-6 7-6s7 2 7 6z"/></svg></span><span class="input">NAME</span></div>
      <div class="field"><span class="icon"><svg viewBox="0 0 16 16"><path d="M3 1l3 3-1.5 2a9 9 0 0 0 5 5L11.5 9.5l3 3L12 15C6 14 2 10 1 4z"/></svg></span><span class="input">MOBILE PHONE</span></div>
      <div class="field"><span class="icon"><svg viewBox="0 0 16 16"><path d="M1 3h14v10H1z M1 3l7 6 7-6" fill="none" stroke="#5c5c5c" stroke-width="1.5"/></svg></span><span class="input">EMAIL</span></div>
      <div class="field"><span class="icon"><svg viewBox="0 0 16 16"><circle cx="8" cy="8" r="6.5" fill="none" stroke="#5c5c5c" stroke-width="1.5"/><circle cx="8" cy="8" r="3.5" fill="none" stroke="#5c5c5c" stroke-width="1.5"/><circle cx="8" cy="8" r="1.2"/></svg></span><span class="input select">SERVICE NEEDED</span></div>
      <div class="field tall"><span class="icon"><svg viewBox="0 0 16 16"><path d="M1 3h14v10H1z M1 3l7 6 7-6" fill="none" stroke="#5c5c5c" stroke-width="1.5"/></svg></span><span class="input area">EMAIL</span></div>
      <span class="submit">Get Quote!</span>
    </form>
  </section>

  <div class="tagline">WHEN IT COMES TO YOUR HOME, THINK <em>BRIGHTPEAK</em></div>

  <section class="about">
    <div class="section-title"><h2>About <span>Brightpeak Roofing</span></h2></div>
    <div class="about-text">
      <p>First of all, thank you for choosing our company. We greatly appreciate your business!</p>
      <p>Let us start off by telling you about our company so you have a better understanding of who we are and how we operate and why you are making the right decision in hiring our company. We are a family owned, owner operated company as well as a Full-Time Professional Roofing Company. We have built our success by providing homeowners as well as small businesses in the entire Chicagoland and Greater Indiana area with quality work at competitive rates and providing the service you should expect from a quality roofing company.</p>
      <p>Brightpeak Roofing &amp; Construction Company, Inc. is committed to giving you the best value when you hire our company to do any project on your home. We are open 7 days a week ensuring you that we will be their when you need us.</p>
      <p class="sign">When it comes to your home, think Brightpeak!</p>
    </div>
    <div class="about-photo"><div role="img" aria-label="Photo of a roofing crew working on a steep tiled roof with dormers"></div></div>
  </section>

  <section class="links-band">
    <a class="link-pill"><span class="pill">View Our Services</span><span class="disc"><svg viewBox="0 0 46 40"><path d="M6 36L14 6h18l8 30z M10 21h26 M8 28h30 M12 13h22 M20 6l-4 30 M26 6l4 30"/></svg></span></a>
    <a class="link-pill"><span class="pill">View Our Projects</span><span class="disc"><svg viewBox="0 0 46 40"><path d="M3 26L23 8l20 18 M11 19v12h24V19" fill="#fff" stroke="#fff"/></svg></span></a>
  </section>

  <section class="advantages">
    <div class="section-title"><h2>Advantages in Hiring <span>Brightpeak Roofing</span></h2></div>
    <div class="adv-list">
      <div class="adv down"><div class="ring"><div class="core"><svg viewBox="0 0 50 50"><circle cx="25" cy="16" r="6"/><path d="M14 40c0-8 5-13 11-13s11 5 11 13z"/><circle cx="11" cy="20" r="4"/><circle cx="39" cy="20" r="4"/></svg></div></div>We are proud to say We Are Family Owned and Operated and have over 30 years of experience</div>
      <div class="adv up"><div class="ring"><div class="core"><svg viewBox="0 0 50 50"><circle cx="24" cy="26" r="16"/><circle cx="24" cy="26" r="9"/><circle cx="24" cy="26" r="2"/><path d="M24 26L42 8 M36 8h6v6"/></svg></div></div>We are fully Licensed, Bonded &amp; Insured</div>
      <div class="adv up" style="margin-top:-30px"><div class="ring"><div class="core"><svg viewBox="0 0 50 50"><path d="M4 32L22 14l18 18 M22 14h12l12 14"/></svg></div></div>We only use the best quality materials that Meet or Exceed all Industry Standards</div>
      <div class="adv up"><div class="ring"><div class="core"><svg viewBox="0 0 50 50"><circle cx="13" cy="14" r="4"/><circle cx="25" cy="14" r="4"/><circle cx="37" cy="14" r="4"/><path d="M8 40V22h10v18 M20 40V22h10v18 M32 40V22h10v18"/></svg></div></div>We are a Second Generation Roofing company</div>
      <div class="adv down" style="margin-top:18px"><div class="ring"><div class="core"><svg viewBox="0 0 50 50"><path d="M12 6h20l6 6v32H12z M17 16h14 M17 22h10"/><circle cx="30" cy="32" r="5"/><path d="M27 36l-2 7 5-3 5 3-2-7"/></svg></div></div>All Warranties will be given in writing to ensure you chose a company you can rely on</div>
      <div class="adv down"><div class="ring"><div class="core"><svg viewBox="0 0 50 50"><path d="M4 24L25 6l21 18 M9 20v22h32V20"/><circle cx="19" cy="28" r="3"/><circle cx="31" cy="28" r="3"/><path d="M14 40c0-5 2-7 5-7s5 2 5 7 M26 40c0-5 2-7 5-7s5 2 5 7"/></svg></div></div>We will give every job the quality, time and craftsmanship as if it were our very own home</div>
    </div>
    <div class="footer-brand">BRIGHTPEAK ROOFING</div>
  </section>

  <footer class="site-footer">
    <div class="fcol col-links">
      <h3>Quick Links</h3>
      <ul><li>Home</li><li>About Brightpeak Roofing</li><li>Services</li><li>Projects</li><li>Contact</li></ul>
    </div>
    <div class="fcol col-services">
      <h3>Services</h3>
      <div class="lists">
        <ul><li>Shingle Roofs</li><li>Flat Roofs</li><li>Roof Repairs</li><li>Storm Damage</li><li>Insurance Work</li></ul>
        <ul><li>Gutters</li><li>Carpentry</li><li>Windows</li><li>Kitchens &amp; Baths</li></ul>
      </div>
    </div>
    <div class="fcol col-contact">
      <h3>Contact Info</h3>
      <div class="line"><svg viewBox="0 0 18 18"><circle cx="9" cy="9" r="8"/><path d="M9 4a3 3 0 0 1 3 3c0 2-3 6-3 6s-3-4-3-6a3 3 0 0 1 3-3z"/></svg><span>BRIGHTPEAK ROOFING<br>123 HARBOR RIDGE DR<br>CHICAGO, IL 60290</span></div>
      <div class="line"><svg viewBox="0 0 18 18"><circle cx="9" cy="9" r="8"/><path d="M5 6h8v6H5z M5 6l4 3 4-3"/></svg><span>BrightpeakRC@example.com</span></div>
    </div>
    <div class="contact-box">
      <h3>CONTACT US TODAY</h3>
      <div class="cb-phone"><svg viewBox="0 0 26 26"><circle cx="13" cy="13" r="12"/><path d="M9 7l2 3-1.5 1.5a8 8 0 0 0 5 5L16 15l3 2-1.5 2.5C12 19 7 14 6.5 8.5z" fill="#fff"/></svg><span><small>Illinois</small><strong>708-555-0142</strong></span></div>
      <div class="cb-phone"><svg viewBox="0 0 26 26"><circle cx="13" cy="13" r="12"/><path d="M9 7l2 3-1.5 1.5a8 8 0 0 0 5 5L16 15l3 2-1.5 2.5C12 19 7 14 6.5 8.5z" fill="#fff"/></svg><span><small>Indiana</small><strong>219-555-0187</strong></span></div>
      <span class="btn">REQUEST A QUOTE</span>
    </div>
  </footer>

  <div class="legal">
    <span>© 2016 Brightpeak Roofing &amp; Construction Company, Inc. All rights reserved.</span>
    <span class="social"><span></span><span></span><span></span><span></span><span></span></span>
  </div>

</div>
</body>
</html>
```